Reed & Vale NC grand opening (for BILLBOARD)

Advertising the grand opening of our cannabis/hemp shop in NC. We will sell all things hemp (flower, cartridges, disposables, edibles, creams, lotions, pet products etc...)

Requirements
Must have
• include, open starting Aug 1, but grand opening Aug 15th.
Nice to have
• Difference slogan ideas "Save some cash, buy our grass" "Find your perfect high at Reed & Vale cannabis store" "Experience Nature's Gift: Reed & Vale Cannabis Store"

```html
<!DOCTYPE html>
<html lang="en">
<head>
<meta charset="utf-8">
<title>Reed &amp; Vale Billboard</title>
<link href="https://fonts.googleapis.com/css2?family=Poppins:wght@500;600;700;800&display=swap" rel="stylesheet">
<style>
  :root {
    --page: #ffffff;
    --green-deep: #062e1a;
    --green-mid: #0a5a2f;
    --green-glow: #0f7a3e;
    --lime: #c8ec3c;
    --white: #ffffff;
    --pill: #7cc443;
    --ink: #0b2414;
    --photo-leaf: #5fa02c;
    --photo-wood: #8a7a6c;
  }
  html, body {
    margin: 0;
    padding: 0;
    width: 1070px;
    height: 1200px;
    overflow: hidden;
    background: var(--page);
  }
  .canvas {
    position: relative;
    width: 1070px;
    height: 1200px;
  }
  .billboard {
    position: absolute;
    left: 35px;
    top: 451px;
    width: 1000px;
    height: 297px;
    overflow: hidden;
    background:
      radial-gradient(ellipse 55% 75% at 48% 18%, var(--green-glow) 0%, var(--green-mid) 45%, transparent 100%),
      linear-gradient(180deg, var(--green-mid) 0%, var(--green-deep) 100%);
    box-shadow: 0 14px 18px -8px rgba(0,0,0,0.35);
    font-family: "Poppins", sans-serif;
  }
  .headline {
    position: absolute;
    left: 36px;
    top: 26px;
    margin: 0;
    font-weight: 800;
    text-transform: uppercase;
  }
  .headline span {
    display: block;
    line-height: 1;
    white-space: nowrap;
  }
  .headline-lead {
    color: var(--lime);
    font-weight: 500;
    font-size: 47px;
    letter-spacing: 0.5px;
  }
  .headline-main {
    color: var(--white);
    font-size: 52px;
    letter-spacing: -1px;
    margin-top: 1px;
  }
  .opening-dates {
    position: absolute;
    left: 38px;
    top: 186px;
    margin: 0;
    color: var(--lime);
    font-weight: 600;
    font-size: 17px;
    line-height: 1;
    letter-spacing: 1.2px;
    text-transform: uppercase;
    white-space: nowrap;
  }
  .brand-name {
    position: absolute;
    left: 37px;
    top: 229px;
    color: var(--white);
    font-weight: 700;
    font-size: 28px;
    line-height: 1;
    white-space: nowrap;
  }
  .location-pill {
    position: absolute;
    left: 266px;
    top: 221px;
    width: 408px;
    height: 39px;
    border-radius: 5px;
    background: var(--pill);
    display: flex;
    align-items: center;
    gap: 7px;
    padding-left: 12px;
    box-sizing: border-box;
    color: var(--ink);
    font-weight: 700;
    font-size: 22px;
    letter-spacing: 2.4px;
    text-transform: uppercase;
    white-space: nowrap;
    z-index: 1;
  }
  .location-pill svg { flex: none; }
  .product-photo {
    position: absolute;
    right: 0;
    top: 8px;
    width: 380px;
    height: 289px;
    background:
      radial-gradient(ellipse 45% 38% at 58% 30%, var(--photo-leaf) 0%, rgba(95,160,44,0.35) 55%, transparent 100%),
      linear-gradient(180deg, transparent 90%, var(--photo-wood) 97%);
  }
</style>
</head>
<body>
  <main class="canvas">
    <section class="billboard">
      <h1 class="headline">
        <span class="headline-lead">Find your perfect</span>
        <span class="headline-main">High at Reed &amp; Vale</span>
        <span class="headline-main">Cannabis Store</span>
      </h1>

      <p class="opening-dates">Open Aug 1 &nbsp;·&nbsp; Grand Opening Aug 15</p>

      <div class="brand-name">Reed &amp; Vale</div>

      <div class="location-pill">
        <svg width="14" height="20" viewBox="0 0 14 20" aria-hidden="true">
          <path d="M7 1C3.7 1 1 3.6 1 6.9 1 11.3 7 19 7 19s6-7.7 6-12.1C13 3.6 10.3 1 7 1z" fill="none" stroke="#0b2414" stroke-width="2.2"/>
          <circle cx="7" cy="7" r="2.2" fill="#0b2414"/>
        </svg>
        <span>Exit 4B Maple Grove Rd</span>
      </div>

      <div class="product-photo" role="img" aria-label="Photo of a cannabis leaf rising from a small shopping cart filled with cannabis buds, resting on a wooden surface"></div>
    </section>
  </main>
</body>
</html>
```